Stationary Set and Logo Update **PAYMENT GUARANTEED**

Stationery Design and Logo Update

About Us

Trindex Supply is a wholesale distributor of OEM [original brand] and compatible [generic brand] parts and supplies for use in copiers, faxes, printers, and multi-function machines. In plain English…we sell all the parts and supplies [such as toner] that make up any office equipment which outputs an image on paper.

Trindex was the 1st distributor to develop and sell a generic brand copier part in the United States. We have been in business since 1972 [nearly 40 years]. Our tagline is "The Steady Choice," as in our company was the first alternative product that copier dealers had to buying original brand copier parts. Trindex is known for offering reliable and cost-effective OEM and compatible products.

Project

We require a fresh, modern and corporate identity. Please submit a stationary package inclusive of a double-sided business card (2" x 3.5"), letterhead (8.5'x11"), and standard #10 envelope (4-1/8” x 9-1/2). You may use our current logo or preferably your take on an updated one. If an attempt is made in updating the logo #004D8E or a similar hue should be used as the primary color.

The design should be clean, simple, modern and professional and make an immediate impact.

Target Market(s)

Copier and printer dealers who lease and service imaging equipment in the United States and Latin America.

Industry/Entity Type

Business

Requirements
Must have
• Simple, clean, modern and professional. Please use #004D8E or a similar hue as the primary color. Letterhead must accommate (2) addresses. We have 2 locations.
Nice to have
• A simple, modern update to our current logo. https://assets.mailvorbo.example/fs030/5520384417702/img/418.jpg
Should not have
• More than (2) colors on logo.

```html
<!DOCTYPE html>
<html lang="en">
<head>
<meta charset="utf-8">
<title>Trindex Supply – Stationery Set</title>
<link rel="stylesheet" href="https://fonts.googleapis.com/css2?family=Arimo:wght@400;700&display=swap">
<style>
  :root {
    --brand-blue: #004d8e;
    --brand-blue-dark: #0a3a72;
    --brand-blue-light: #0b5aa3;
    --paper: #ffffff;
    --stage: #ffffff;
    --text-gray: #7a7a7a;
    --text-dark: #444444;
    --rule-gray: #c8c8c8;
    --shadow: rgba(0, 0, 0, 0.18);
  }
  * { box-sizing: border-box; margin: 0; padding: 0; }
  html, body { width: 1200px; height: 800px; overflow: hidden; background: var(--stage); }
  body { font-family: "Arimo", Arial, sans-serif; position: relative; }

  .sheet { position: absolute; box-shadow: 0 1px 4px var(--shadow); overflow: hidden; }
  .sheet--blue { background: linear-gradient(120deg, var(--brand-blue-dark) 0%, var(--brand-blue) 55%, var(--brand-blue-light) 100%); }
  .sheet--white { background: var(--paper); }

  .wordmark { display: flex; align-items: center; gap: 5px; font-weight: 700; color: var(--brand-blue); line-height: 1; white-space: nowrap; }
  .wordmark__dot { border-radius: 50%; background: currentColor; flex: none; }
  .wordmark--white { color: #ffffff; }

  .address-block { display: flex; gap: 8px; font-size: 6px; line-height: 1.45; color: var(--text-gray); white-space: nowrap; width: max-content; }
  .address-block__col + .address-block__col { border-left: 1px solid var(--rule-gray); padding-left: 8px; }
  .address-block--white { color: rgba(255,255,255,0.85); }
  .address-block--white .address-block__col + .address-block__col { border-left-color: rgba(255,255,255,0.5); }

  /* Business card front */
  .card-front { left: 52px; top: 52px; width: 304px; height: 160px; }
  .card-front .wordmark { position: absolute; left: 24px; top: 62px; font-size: 34px; gap: 7px; }
  .card-front .wordmark__dot { width: 22px; height: 22px; }

  /* Business card back */
  .card-back { left: 364px; top: 28px; width: 304px; height: 184px; }
  .card-back__name { position: absolute; left: 8px; top: 80px; font-size: 9px; font-weight: 700; color: var(--brand-blue); }
  .card-back__title { position: absolute; left: 8px; top: 91px; font-size: 6px; color: var(--brand-blue); }
  .card-back .wordmark { position: absolute; left: 8px; top: 118px; font-size: 15px; gap: 3px; }
  .card-back .wordmark__dot { width: 10px; height: 10px; }
  .card-back .address-block { position: absolute; left: 84px; top: 114px; }

  /* Letterhead back */
  .letter-back { left: 28px; top: 224px; width: 428px; height: 564px; }
  .letter-back .wordmark { position: absolute; left: 24px; top: 482px; font-size: 30px; gap: 6px; }
  .letter-back .wordmark__dot { width: 20px; height: 20px; }
  .letter-back .address-block { position: absolute; left: 172px; top: 478px; font-size: 6.5px; }

  /* Letterhead front */
  .letter-front { left: 468px; top: 224px; width: 424px; height: 564px; }
  .letter-front .wordmark { position: absolute; right: 52px; top: 42px; font-size: 20px; gap: 4px; }
  .letter-front .wordmark__dot { width: 13px; height: 13px; }
  .letter-front__name { position: absolute; right: 52px; top: 68px; font-size: 7px; font-weight: 700; color: var(--brand-blue); text-align: right; }
  .letter-front__title { position: absolute; right: 52px; top: 78px; font-size: 5.5px; color: var(--brand-blue); }
  .letter-body { position: absolute; left: 52px; top: 190px; width: 320px; font-size: 5.5px; line-height: 1.9; color: var(--text-gray); }
  .letter-body__recipient { margin-bottom: 14px; }
  .letter-body__subject { font-weight: 700; color: var(--text-dark); font-size: 6px; margin-bottom: 14px; }
  .letter-body p { margin-bottom: 12px; }
  .letter-signoff { position: absolute; left: 140px; top: 454px; font-size: 5.5px; color: var(--text-gray); }
  .letter-signoff svg { display: block; margin-top: 2px; }

  /* Envelope */
  .envelope { left: 912px; top: 116px; width: 256px; height: 668px; }
  .envelope__flap { position: absolute; left: 0; top: 0; }
  .envelope__rotated { position: absolute; transform-origin: top left; transform: rotate(90deg); white-space: nowrap; width: max-content; }
  .envelope__return { left: 232px; top: 250px; }
  .envelope__return .address-block { font-size: 6.5px; }
  .envelope__brand { left: 246px; top: 500px; }
  .envelope__brand .wordmark { font-size: 30px; gap: 6px; }
  .envelope__brand .wordmark__dot { width: 20px; height: 20px; }
</style>
</head>
<body>

<section class="sheet sheet--blue card-front" aria-label="Business card front">
  <div class="wordmark wordmark--white"><span class="wordmark__dot"></span>Trindex</div>
</section>

<section class="sheet sheet--white card-back" aria-label="Business card back">
  <div class="card-back__name">Marena Oduya</div>
  <div class="card-back__title">Marketing Coordinator</div>
  <div class="wordmark"><span class="wordmark__dot"></span>Trindex</div>
  <div class="address-block">
    <div class="address-block__col">
      Corporate Office<br>2150 Harlow Street<br>Dunmore, FL 33019<br>Toll Free: 800.555.0142<br>Direct: 954.555.0187<br>Email: moduya@trindex.example
    </div>
    <div class="address-block__col">
      West Coast Fulfillment Center<br>North Ridge Commerce Park #2<br>740 Ridgeline Way<br>Calder, NV 89420
    </div>
  </div>
</section>

<section class="sheet sheet--blue letter-back" aria-label="Letterhead reverse">
  <div class="wordmark wordmark--white"><span class="wordmark__dot"></span>Trindex</div>
  <div class="address-block address-block--white">
    <div class="address-block__col">
      Corporate Office<br>2150 Harlow Street<br>Dunmore, FL 33019<br>Toll Free: 800.555.0142<br>Direct: 954.555.0187<br>Email: moduya@trindex.example
    </div>
    <div class="address-block__col">
      West Coast Fulfillment Center<br>North Ridge Commerce Park #2<br>740 Ridgeline Way<br>Calder, NV 89420
    </div>
  </div>
</section>

<section class="sheet sheet--white letter-front" aria-label="Letterhead front">
  <div class="wordmark"><span class="wordmark__dot"></span>Trindex</div>
  <div class="letter-front__name">Marena Oduya</div>
  <div class="letter-front__title">Marketing Coordinator</div>
  <div class="letter-body">
    <div class="letter-body__recipient">To:<br>Name Surname<br>Street address</div>
    <div class="letter-body__subject">Re: updated pricing for compatible copier parts and toner supplies</div>
    <p>Thank you for your continued partnership. Our compatible parts program now covers more copier and printer models than ever, with consistent quality and fast shipping from both of our locations to dealers across the country.</p>
    <p>Enclosed you will find our current catalog and price sheet. Please review the new toner listings and contact your account manager with any questions. We are glad to arrange samples, volume quotes and service support for your technicians at any time this quarter.</p>
  </div>
  <div class="letter-signoff">
    Sincerely, Marena Oduya
    <svg width="60" height="16" viewBox="0 0 60 16" aria-hidden="true">
      <path d="M2 12 C8 2, 12 2, 14 10 S22 14, 28 6 S40 4, 44 10 S54 12, 58 6" fill="none" stroke="#555" stroke-width="1"/>
    </svg>
  </div>
</section>

<section class="sheet sheet--white envelope" aria-label="Number 10 envelope">
  <svg class="envelope__flap" width="256" height="160" viewBox="0 0 256 160" aria-hidden="true">
    <polyline points="0,22 128,150 256,22" fill="none" stroke="#e2e2e2" stroke-width="1.5"/>
  </svg>
  <div class="envelope__rotated envelope__return">
    <div class="address-block">
      <div class="address-block__col">
        Corporate Office<br>2150 Harlow Street<br>Dunmore, FL 33019<br>Toll Free: 800.555.0142<br>Direct: 954.555.0187<br>Email: moduya@trindex.example
      </div>
      <div class="address-block__col">
        West Coast Fulfillment Center<br>North Ridge Commerce Park #2<br>740 Ridgeline Way<br>Calder, NV 89420
      </div>
    </div>
  </div>
  <div class="envelope__rotated envelope__brand">
    <div class="wordmark"><span class="wordmark__dot"></span>Trindex</div>
  </div>
</section>

</body>
</html>
```